KT Design Business Card

I would like a business card similar to this
https://www.artquorra.com/design/8173920
with my info and a picture of my rifle. You can use something like this
https://www.snaplirra.com/pin/381926405572018843/visual-search/?cropSource=6&h=476&w=268&x=12&y=12
or
https://www.snaplirra.com/pin/219604837751093468/

I have a logo, it is a shepperds staff. I build custom rifles and do Law Enforcement sales. Some where on the card it needs to say something like, "Custom AR's built correctly", "All rifles come with honed uppers and bedded barrels", "All rifles are fully tested and come with a 3 shot card", "Law Enforcement models are available", "Tactical Equipment Consulting", "One stop shop for all tactical equipment"

Business Name: KT Design LLC
Name: Brent Hollis
Phone: (555) 614-2980
Email: brent.ktdesign@mailbriq.com
Address: 3082 Tamblin Ct., Marlow Bend, SC, 29815

Just use the concept of the staff in the attachments the other stuff is not related

```html
<!DOCTYPE html>
<html lang="en">
<head>
<meta charset="utf-8">
<title>KT Design Business Card</title>
<link rel="stylesheet" href="https://fonts.googleapis.com/css2?family=Source+Sans+3:wght@400;600;700&display=swap">
<style>
  :root {
    --page-bg: #e9e6e2;
    --card-black: #1c1c1c;
    --ink-white: #f4f2ef;
    --ink-soft: #d9d5d0;
    --accent-tan: #b8968a;
    --photo-dark: #3a3a30;
    --photo-mid: #6b6450;
    --photo-light: #a89a86;
    --divider: #6a6a6a;
  }
  * { box-sizing: border-box; margin: 0; padding: 0; }
  html, body {
    width: 1200px; height: 960px; overflow: hidden;
    background: var(--page-bg);
    font-family: "Source Sans 3", Arial, sans-serif;
  }
  .canvas { position: relative; width: 1200px; height: 960px; }

  .card {
    position: absolute; left: 220px; width: 760px; height: 434px;
    background: var(--card-black);
    border-radius: 22px; overflow: hidden;
    box-shadow: 0 6px 18px rgba(0,0,0,0.18);
  }
  .card--front { top: 31px; }
  .card--back { top: 495px; }

  /* Front */
  .front-art { position: absolute; inset: 0; }
  .front-features {
    position: absolute; left: 350px; right: 20px; top: 160px;
    list-style: none; text-align: center; white-space: nowrap;
    color: var(--ink-white); font-size: 18px; line-height: 1.5;
  }

  /* Back */
  .brand-block {
    position: absolute; left: 0; top: 0; width: 300px; height: 100%;
    display: flex; flex-direction: column; align-items: center; justify-content: center;
    color: var(--ink-white);
  }
  .brand-name {
    display: flex; align-items: center; gap: 10px;
    font-size: 34px; font-weight: 600; letter-spacing: 0.5px; text-transform: uppercase;
  }
  .brand-dot { width: 12px; height: 12px; border-radius: 50%; background: var(--ink-white); }
  .model-info {
    margin-top: 10px; text-align: center;
    font-size: 19px; line-height: 1.15; text-transform: uppercase; color: var(--ink-soft);
  }
  .divider {
    position: absolute; left: 300px; top: 90px; width: 1px; height: 254px;
    background: var(--divider);
  }
  .contact-block {
    position: absolute; left: 340px; top: 98px; color: var(--ink-white);
  }
  .person-name {
    font-size: 30px; font-weight: 700; text-transform: uppercase; letter-spacing: 0.5px;
  }
  .company-address { margin-top: 18px; font-size: 20px; line-height: 1.25; color: var(--ink-soft); font-style: normal; }
  .company-address .company { color: var(--ink-white); font-weight: 600; }
  .contact-list { margin-top: 18px; list-style: none; font-size: 19px; line-height: 1.45; color: var(--ink-soft); }
  .contact-list li { display: flex; align-items: center; gap: 12px; white-space: nowrap; }
  .contact-icon { width: 16px; height: 16px; flex: none; fill: var(--ink-white); }
</style>
</head>
<body>
<main class="canvas">

  <section class="card card--front" aria-label="Card front">
    <svg class="front-art" width="760" height="434" viewBox="0 0 760 434">
      <defs>
        <linearGradient id="photoTone" x1="0" y1="0" x2="1" y2="1">
          <stop offset="0" stop-color="#a89a86"/>
          <stop offset="0.45" stop-color="#6b6450"/>
          <stop offset="1" stop-color="#3a3a30"/>
        </linearGradient>
      </defs>
      <polygon points="0,0 420,0 232,434 0,434" fill="url(#photoTone)" role="img" aria-label="Photo of a custom AR rifle resting on olive tactical gear"/>
      <polygon points="420,0 446,0 258,434 232,434" fill="#b8968a"/>
    </svg>
    <ul class="front-features">
      <li>Custom AR's built correctly</li>
      <li>All rifles come with honed uppers &amp; bedded barrels</li>
      <li>All rifles are fully tested &amp; come with a 3 shot card</li>
      <li>Law Enforcement models are available</li>
      <li>Tactical Equipment Consulting</li>
      <li>One stop shop for all tactical equipment</li>
    </ul>
  </section>

  <section class="card card--back" aria-label="Card back">
    <div class="brand-block">
      <div class="brand-name"><span class="brand-dot"></span>KT Design</div>
      <div class="model-info">
        <div>KTD 15</div>
        <div>Multi Cal</div>
        <div>S/N: XXXXX</div>
      </div>
    </div>
    <div class="divider"></div>
    <div class="contact-block">
      <h1 class="person-name">Brent Hollis</h1>
      <address class="company-address">
        <div class="company">KT Design LLC</div>
        <div>3082 Tamblin Ct.</div>
        <div>Marlow Bend, SC, 29815</div>
      </address>
      <ul class="contact-list">
        <li>
          <svg class="contact-icon" viewBox="0 0 16 16" aria-hidden="true"><path d="M3.6 1.2l2.3 2.6-1.2 1.6c.9 2 2.3 3.5 4.4 4.5l1.6-1.2 2.6 2.3-1.1 2.6C7 13.6 2.2 8.8 1 4.2z"/></svg>
          (555) 614-2980
        </li>
        <li>
          <svg class="contact-icon" viewBox="0 0 16 16" aria-hidden="true"><path d="M1 3h14v10H1z M2 4.2v.3l6 4 6-4v-.3z" fill-rule="evenodd"/></svg>
          brent.ktdesign@mailbriq.com
        </li>
        <li>
          <svg class="contact-icon" viewBox="0 0 16 16" aria-hidden="true"><circle cx="8" cy="8" r="7"/><path d="M1 8h14M8 1c3 3 3 11 0 14M8 1c-3 3-3 11 0 14" stroke="#1c1c1c" stroke-width="1.2" fill="none"/></svg>
          www.ktdesignworks.com
        </li>
      </ul>
    </div>
  </section>

</main>
</body>
</html>
```